Poster of Core Values & Motto

Create our core values poster and motto. Attached are our core values and our Motto. This poster represents both of our companies Tidy Pulp & CuraBinix.

Target Market(s)

Our team / employees

Industry/Entity Type

Shredding and Medical Waste

Colors
59FF00
82FF00
B8FF75
E3FFCB
F4FFEA
EB3D1F
EC4F4E
F09395
F8D3D4
FCEDEE

Requirements
Must have
• Include both companies logos

```html
<!DOCTYPE html>
<html lang="en">
<head>
<meta charset="utf-8">
<title>Core Values Poster</title>
<link href="https://fonts.googleapis.com/css2?family=Montserrat:wght@300;400;600;700;800&display=swap" rel="stylesheet">
<style>
  :root {
    --stage: #bdbdbd;
    --navy: #0b1f30;
    --green: #0cab4f;
    --green-ink: #0a2a1f;
    --teal-tag: #22cfc0;
    --teal-cell: #00a19a;
    --sky: #2fb6e0;
    --ink: #0b1f30;
    --white: #ffffff;
    --cell-text: #d7f4f1;
    --band: #d0d0d0;
    --brand-ink: #1b2b38;
  }
  * { box-sizing: border-box; margin: 0; padding: 0; }
  html, body { width: 1200px; height: 800px; overflow: hidden; }
  body { background: var(--stage); font-family: "Montserrat", sans-serif; position: relative; }

  .poster {
    position: absolute; left: 347px; top: 20px;
    width: 506px; height: 760px;
    background: var(--navy); overflow: hidden;
  }
  .helix-art {
    position: absolute; left: 181px; top: 0; width: 325px; height: 499px;
    background:
      radial-gradient(ellipse 30% 45% at 50% 45%, rgba(60,220,200,.55), rgba(30,140,200,.25) 55%, transparent 80%),
      radial-gradient(ellipse 45% 25% at 70% 30%, rgba(40,130,210,.35), transparent 75%),
      radial-gradient(ellipse 40% 30% at 30% 15%, rgba(40,120,200,.3), transparent 75%);
  }

  .motto-words { position: absolute; left: 45px; top: 98px; }
  .motto-word {
    display: block; background: var(--green); color: var(--green-ink);
    font-weight: 800; font-size: 18px; line-height: 29px; height: 29px;
    padding-left: 9px; margin-bottom: 4px; letter-spacing: .3px;
  }
  .motto-word.purpose { width: 126px; }
  .motto-word.cause { width: 95px; }
  .motto-word.passion { width: 118px; }

  .tagline {
    position: absolute; left: 45px; top: 214px;
    color: var(--sky); font-weight: 300; font-size: 17px; line-height: 22px;
  }

  .values-tag {
    position: absolute; left: 178px; top: 307px; width: 149px; height: 29px;
    background: var(--teal-tag); color: var(--ink);
    font-weight: 700; font-size: 13px; line-height: 29px; text-align: center;
  }

  .values-grid {
    position: absolute; left: 45px; top: 356px;
    display: grid; grid-template-columns: repeat(3, 134px); grid-template-rows: repeat(2, 133px);
    column-gap: 8px; row-gap: 9px;
  }
  .value-card {
    background: var(--teal-cell); text-align: center; color: var(--white);
    padding-top: 22px;
  }
  .value-icon { width: 28px; height: 28px; display: block; margin: 0 auto; }
  .value-title { font-weight: 700; font-size: 8px; margin-top: 12px; letter-spacing: .2px; }
  .value-rule { width: 12px; height: 1px; background: var(--ink); margin: 4px auto 0; }
  .value-text {
    font-weight: 400; font-size: 6.5px; line-height: 9px; color: var(--cell-text);
    margin: 10px auto 0; width: 90px;
  }

  .brand-band {
    position: absolute; left: 45px; top: 662px; width: 418px; height: 67px;
    background: var(--band);
    display: flex; align-items: center; justify-content: center; gap: 46px;
  }
  .brand-name { font-weight: 700; font-size: 15px; color: var(--brand-ink); display: flex; align-items: center; gap: 6px; }
  .brand-dot { width: 10px; height: 10px; border-radius: 50%; display: inline-block; }
  .brand-dot.pulp { background: var(--green); }
  .brand-dot.cura { background: #eb3d1f; }
</style>
</head>
<body>
  <main class="poster">
    <div class="helix-art" role="img" aria-label="Glowing blue and teal DNA double helix made of light particles"></div>

    <div class="motto-words">
      <span class="motto-word purpose">PURPOSE</span>
      <span class="motto-word cause">CAUSE</span>
      <span class="motto-word passion">PASSION</span>
    </div>

    <p class="tagline">Remind people<br>what great service<br>looks like</p>

    <div class="values-tag">CORE VALUES</div>

    <section class="values-grid">
      <article class="value-card">
        <svg class="value-icon" viewBox="0 0 28 28" fill="none" stroke="#0b1f30" stroke-width="1.4">
          <circle cx="6" cy="8" r="3"/><circle cx="14" cy="8" r="3"/><circle cx="22" cy="8" r="3"/>
          <path d="M2 22v-5a4 4 0 0 1 8 0M10 22v-5a4 4 0 0 1 8 0M18 22v-5a4 4 0 0 1 8 0M4 19h20"/>
        </svg>
        <h3 class="value-title">SYNERGY / TEAMWORK</h3>
        <div class="value-rule"></div>
        <p class="value-text">Remind people what great service looks like</p>
      </article>
      <article class="value-card">
        <svg class="value-icon" viewBox="0 0 28 28" fill="none" stroke="#0b1f30" stroke-width="1.4">
          <circle cx="14" cy="10" r="7"/><circle cx="14" cy="10" r="3.5"/>
          <path d="M9 16l-3 8 4-1.5 2 3 2-6M19 16l3 8-4-1.5-2 3-2-6"/>
        </svg>
        <h3 class="value-title">EXCELLENCE</h3>
        <div class="value-rule"></div>
        <p class="value-text">Exceed expectations with a smile</p>
      </article>
      <article class="value-card">
        <svg class="value-icon" viewBox="0 0 28 28" fill="none" stroke="#0b1f30" stroke-width="1.4">
          <circle cx="14" cy="14" r="4"/>
          <path d="M14 7v2M14 19v2M7 14h2M19 14h2M9 9l1.4 1.4M17.6 17.6L19 19M9 19l1.4-1.4M17.6 10.4L19 9"/>
          <path d="M4 12a10 10 0 0 1 18-5M24 16a10 10 0 0 1-18 5"/>
          <path d="M22 3v4h-4M6 25v-4h4"/>
        </svg>
        <h3 class="value-title">SYNERGY / TEAMWORK</h3>
        <div class="value-rule"></div>
        <p class="value-text">On-Time, Sense of urgency, always trying to improve</p>
      </article>
      <article class="value-card">
        <svg class="value-icon" viewBox="0 0 28 28" fill="none" stroke="#0b1f30" stroke-width="1.4">
          <path d="M14 3l9 3.5v7c0 6-4 9.5-9 11.5-5-2-9-5.5-9-11.5v-7z"/>
          <path d="M10 14l3 3 5-6"/>
        </svg>
        <h3 class="value-title">SYNERGY / TEAMWORK</h3>
        <div class="value-rule"></div>
        <p class="value-text">We are just as secure as an armored truck with money</p>
      </article>
      <article class="value-card">
        <svg class="value-icon" viewBox="0 0 28 28" fill="none" stroke="#0b1f30" stroke-width="1.4">
          <path d="M9 3h10l6 6v10l-6 6H9l-6-6V9z"/>
          <path d="M10 14l3 3 5-6"/>
        </svg>
        <h3 class="value-title">SYNERGY / TEAMWORK</h3>
        <div class="value-rule"></div>
        <p class="value-text">Do the right thing</p>
      </article>
      <article class="value-card">
        <svg class="value-icon" viewBox="0 0 28 28" fill="none" stroke="#0b1f30" stroke-width="1.4">
          <rect x="3" y="12" width="5" height="12"/>
          <path d="M8 13l5-8c2 0 3 1.5 2.5 3.5L15 12h7a2 2 0 0 1 2 2.5l-2 8a2 2 0 0 1-2 1.5H8"/>
        </svg>
        <h3 class="value-title">SYNERGY / TEAMWORK</h3>
        <div class="value-rule"></div>
        <p class="value-text">Do what you say you will do</p>
      </article>
    </section>

    <footer class="brand-band">
      <span class="brand-name"><i class="brand-dot pulp"></i>Tidy Pulp</span>
      <span class="brand-name"><i class="brand-dot cura"></i>CuraBinix</span>
    </footer>
  </main>
</body>
</html>
```